Restaurant needs a vertical banner for fried catfish

Our restaurant is looking for an eye-catching 78.75in. x 36in. vertical physical banner ad for our fried catfish. Photos for the fried catfish will be provided as a reference but we will also accept anything similar to the photo. We will be using the following as our receptacle: https://www.plankoria.example/banner-stand/retractable-banner-stands/
The design must incorporate the following flavor texts:
Fried Catfish
Always Fresh!
Made from Scratch
Hand-cut Fillets
The Best Catfish in Texas
Served with fries, hush puppies, and a 32oz fountain drink
Also available by the pound!
The final design should be creative, professional, and eye-catching for customers.
Updates
Colors
Designer to choose colors to be used in the design.
Requirements
Must have
- We are open to any and all design elements, albeit the 'flavor texts' should not overpower, but complement the fried catfish photo. 'Fried Catfish' can be used in lieu of a main title/logo.
Nice to have
- Transparent or textured backgrounds that can encompass any or all part of the banner such as a cutting board, shadows, abstract, etc to show depth are a plus.
- Use of vectors or objects such as ribbons or shapes to encapsulate the 'flavor texts' are also encouraged.

```html
<!DOCTYPE html>
<html lang="en">
<head>
<meta charset="utf-8">
<title>Fried Catfish – Vertical Banner</title>
<link rel="stylesheet" href="https://fonts.googleapis.com/css2?family=Great+Vibes&family=Signika:wght@600&display=swap">
<style>
  :root {
    --page-bg: #f2f2f2;
    --sky-light: #8fd4f5;
    --sky-cyan: #12a9e6;
    --sky-steel: #4a9ad8;
    --accent-pink: #e2376b;
    --title-red: #e8435f;
    --script-dark: #2f2f38;
    --slate: #4a4a4c;
    --slate-dark: #3a3a3c;
    --mustard: #fcc72b;
    --copy-dark: #2a2420;
    --photo-warm: #b0702e;
    --photo-deep: #5a3a1e;
    --photo-light: #e9d6b4;
  }
  html, body {
    margin: 0;
    padding: 0;
    width: 1200px;
    height: 1200px;
    overflow: hidden;
    background: var(--page-bg);
  }
  .canvas {
    width: 1200px;
    height: 1200px;
    display: flex;
    align-items: center;
    justify-content: center;
  }
  .banner {
    width: 503px;
    height: 1090px;
    display: block;
    box-shadow: 6px 6px 14px rgba(0, 0, 0, 0.25);
  }
  .banner-title {
    font-family: "Great Vibes", cursive;
    font-size: 54px;
    fill: var(--title-red);
    stroke: #ffffff;
    stroke-width: 1.2px;
    paint-order: stroke;
  }
  .banner-tagline {
    font-family: "Great Vibes", cursive;
    font-size: 27px;
    fill: var(--script-dark);
  }
  .feature-text {
    font-family: "Signika", sans-serif;
    font-weight: 600;
    font-size: 16.5px;
    fill: var(--copy-dark);
  }
  .ribbon { fill: var(--accent-pink); }
</style>
</head>
<body>
<main class="canvas">
  <svg class="banner" viewBox="0 0 340 737" xmlns="http://www.w3.org/2000/svg" aria-label="Fried Catfish vertical banner">
    <defs>
      <linearGradient id="photoTone" x1="0" y1="0" x2="0" y2="1">
        <stop offset="0" stop-color="var(--photo-light)"/>
        <stop offset="0.35" stop-color="var(--photo-warm)"/>
        <stop offset="0.75" stop-color="var(--photo-deep)"/>
        <stop offset="1" stop-color="var(--photo-light)"/>
      </linearGradient>
      <g id="ribbonMark">
        <path d="M0 0 L26 -6 L26 6 L0 12 L6 6 Z"/>
      </g>
    </defs>

    <!-- header block -->
    <g class="header">
      <rect x="0" y="0" width="340" height="158" fill="var(--sky-light)"/>
      <polygon points="18,0 200,0 230,158 40,158 0,50 0,0" fill="var(--sky-cyan)"/>
      <polygon points="140,0 340,0 340,158 210,158" fill="var(--sky-steel)"/>
      <text class="banner-title" x="22" y="96">Fried Catfish</text>
      <text class="banner-tagline" x="168" y="124" text-anchor="middle">Always Fresh!</text>
    </g>

    <!-- food photo band -->
    <rect x="0" y="156" width="340" height="4" fill="var(--accent-pink)"/>
    <rect x="0" y="160" width="340" height="208" fill="url(#photoTone)" role="img"
          aria-label="Photo of fried catfish fillets on fries with hush puppies and tartar sauce, tomatoes, onions and lemons behind"/>
    <rect x="0" y="367" width="340" height="3" fill="var(--accent-pink)"/>

    <!-- feature panel -->
    <g class="feature-panel">
      <rect x="0" y="370" width="340" height="367" fill="var(--slate)"/>
      <polygon points="280,370 340,370 340,560 310,600" fill="var(--slate-dark)"/>
      <polygon points="37,373 300,373 338,612 318,718 37,680" fill="var(--mustard)"/>
      <polygon points="240,737 340,622 340,737" fill="var(--sky-light)"/>
    </g>

    <g class="ribbons">
      <use href="#ribbonMark" class="ribbon" x="10" y="406"/>
      <use href="#ribbonMark" class="ribbon" x="10" y="453"/>
      <use href="#ribbonMark" class="ribbon" x="10" y="499"/>
      <use href="#ribbonMark" class="ribbon" x="10" y="546"/>
      <use href="#ribbonMark" class="ribbon" x="10" y="638"/>
    </g>

    <g class="feature-list">
      <text class="feature-text" x="42" y="416">Made from Scratch</text>
      <text class="feature-text" x="42" y="463">Hand-cut Fillets</text>
      <text class="feature-text" x="42" y="509">The Best Catfish in Texas</text>
      <text class="feature-text" x="42" y="556">Served with fries, hush puppies,</text>
      <text class="feature-text" x="42" y="602">and a 32oz fountain drink</text>
      <text class="feature-text" x="42" y="648">Also available by the pound!</text>
    </g>
  </svg>
</main>
</body>
</html>
```